Lawn Sign Design – Vextra

We need a clean, eye-catching 18" x 24" lawn sign for Vextra that effectively communicates our core message while maintaining strong brand consistency.

Key Elements to Include:
Tagline (Main Focus): Upgrade Your Roof Without Replacing It
Website: www.tryvextra-example.com
Phone Number: (877) VEXTRA-GO
PRQT License Number: 4830517
Vextra Logo & Branding: Ensure the logo, corporate colors, and custom font are used consistently to align with our existing branding.

Design Guidelines:
Simple & High-Impact: The tagline should be the most prominent element on the sign, drawing immediate attention.
Easy Readability: Use a bold, clean design with high contrast for quick readability from a distance.
Balanced Layout: Place supporting details (website, phone number, and PRQT number) in a visually clear but secondary position to the tagline.
Professional & Modern: The sign should reflect credibility and innovation in the roofing industry.

Deliverables:
High-resolution print-ready files (CMYK)
A digital proof for review before finalizing
The final design should make a strong impression with minimal text, ensuring that anyone passing by can instantly grasp what we offer.

I am including our custom font. To get an hexagon in our name, simply type the $ after the 'O" Please use this font for anything you type.

```html
<!DOCTYPE html>
<html lang="en">
<head>
<meta charset="utf-8">
<title>Vextra Lawn Sign</title>
<link rel="stylesheet" href="https://fonts.googleapis.com/css2?family=Nunito:wght@700;800;900&display=swap">
<style>
  :root {
    --brand-blue: #17519a;
    --brand-dark: #2e333c;
    --sign-white: #ffffff;
    --backdrop: #eef0f3;
  }
  html, body {
    margin: 0;
    padding: 0;
    width: 1200px;
    height: 1200px;
    overflow: hidden;
    background: var(--backdrop);
  }
  .canvas {
    width: 1200px;
    height: 1200px;
    display: flex;
    align-items: center;
    justify-content: center;
  }
  .lawn-sign {
    display: block;
    width: 824px;
    height: 1100px;
    box-shadow: 0 6px 24px rgba(0, 0, 0, 0.12);
  }
  .sign-text {
    font-family: "Nunito", sans-serif;
  }
  .brand-name { fill: var(--brand-blue); font-weight: 900; font-size: 104px; letter-spacing: 3px; }
  .tagline { fill: var(--sign-white); font-weight: 900; font-size: 86px; }
  .phone-number { fill: var(--sign-white); font-weight: 800; font-size: 66px; }
  .license-label { fill: var(--sign-white); font-weight: 800; font-size: 34px; }
  .license-number { fill: var(--brand-blue); font-weight: 900; font-size: 56px; letter-spacing: 1px; }
  .website { fill: var(--sign-white); font-weight: 800; font-size: 42px; letter-spacing: 1px; }
  .fill-blue { fill: var(--brand-blue); }
  .fill-dark { fill: var(--brand-dark); }
  .fill-white { fill: var(--sign-white); }
  .phone-frame { fill: none; stroke: var(--sign-white); stroke-width: 2; }
</style>
</head>
<body>
<main class="canvas">
  <svg class="lawn-sign" viewBox="0 0 925 1235" xmlns="http://www.w3.org/2000/svg" aria-label="Vextra lawn sign">
    <!-- header -->
    <rect class="fill-white" x="0" y="0" width="925" height="445"/>
    <circle class="fill-blue" cx="462" cy="175" r="62"/>
    <text class="sign-text brand-name" x="462" y="398" text-anchor="middle" textLength="440" lengthAdjust="spacingAndGlyphs">VEXTRA</text>

    <!-- header corner bands -->
    <polygon class="fill-dark" points="0,357 99,357 157,445 0,445"/>
    <polygon class="fill-blue" points="99,357 137,357 201,445 157,445"/>
    <polygon class="fill-dark" points="829,357 925,357 925,445 767,445"/>
    <polygon class="fill-blue" points="779,357 829,357 767,445 716,445"/>

    <!-- tagline panel -->
    <rect class="fill-blue" x="0" y="444" width="925" height="516"/>
    <text class="sign-text tagline" x="462" y="570" text-anchor="middle" textLength="735" lengthAdjust="spacingAndGlyphs">UPGRADE YOUR</text>
    <text class="sign-text tagline" x="462" y="661" text-anchor="middle" textLength="745" lengthAdjust="spacingAndGlyphs">ROOF WITHOUT</text>
    <text class="sign-text tagline" x="462" y="752" text-anchor="middle" textLength="634" lengthAdjust="spacingAndGlyphs">REPLACING IT</text>

    <!-- phone box -->
    <rect class="phone-frame" x="79" y="792" width="767" height="128"/>
    <g class="phone-icon">
      <circle class="fill-white" cx="162" cy="855" r="31"/>
      <path class="fill-blue" d="M150 840c2-2 5-2 6 0l4 6c1 2 1 4-1 5l-3 2c2 5 6 9 11 11l2-3c1-2 3-2 5-1l6 4c2 1 2 4 0 6l-3 3c-3 3-8 3-12 1-9-5-16-12-20-21-2-4-2-9 1-12z"/>
    </g>
    <text class="sign-text phone-number" x="209" y="879" textLength="585" lengthAdjust="spacingAndGlyphs">(877) VEXTRA-GO</text>

    <!-- license band -->
    <rect class="fill-white" x="0" y="960" width="925" height="147"/>
    <polygon class="fill-blue" points="0,980 497,980 565,1107 0,1107"/>
    <text class="sign-text license-label" x="92" y="1056" textLength="387" lengthAdjust="spacingAndGlyphs">PRQT License Number:</text>
    <text class="sign-text license-number" x="591" y="1058" textLength="243" lengthAdjust="spacingAndGlyphs">4830517</text>

    <!-- footer -->
    <rect class="fill-dark" x="0" y="1107" width="925" height="128"/>
    <text class="sign-text website" x="462" y="1184" text-anchor="middle">www.tryvextra-example.com</text>
  </svg>
</main>
</body>
</html>
```